We need a flyer where we promote a workshop to our members of the jewish community www.vbq-gemeinde.example . The workshop is calles "command in seven weeks presented by VBQ. We would like to see a flyer with the below text is used and also some pictures (attached). The flyer should come over as cool, fresh, innovative for a younger crowd so called young professionals (age 28-35).
TITLE.
"Command in Seven Weeks.
SUBTITLE.
Your systematic self-coaching roadmap to power and impact—and your future.”
TEXT.
Dr. Marcus L. Brandauer is the CEO Emeritus of Alpine Advisory Partners—he made an exit in 2013. He is the award-winning author of 8 books, including "Momentum-By-Design," "Speak Up or Fade" and "The Cantor and the Chairman.”
For the past 20 years he has taught leadership at Harwick University in New York and at KLB (Lindmoor University) to prepare future CEOs and other leaders in business, government , nonprofits and the military.
Now, in a process exclusively designed for VBQ’s next generation of emerging leaders, Marcus unpacks his leadership secrets in 3 action-packed labs—reduced to the max:
Lab 1. Command in Seven Weeks: The Summit Compass Model®. Self-Assessment. Self-Leadership: “The Lantern.” 5-Year Vision. 100-Day Catalytic Project.
Lab 2. Guiding Through Words. Relationship: Building Trust. Momentum-By-Design. Cockpit.
Lab 3. Debrief and Scale-Up. Sustainability. Action Tools.
Do you want to build your own future and a life you love? Do you want to jump-start that future and life over 100 days while learning a toolbox of leadership skills, networking with like-minded people—and even get some pizza? Then join us.
young professionals age 28-35

```html
<!DOCTYPE html>
<html lang="en">
<head>
<meta charset="utf-8">
<title>Command in Seven Weeks – VBQ Workshop Flyer</title>
<link rel="stylesheet" href="https://fonts.googleapis.com/css2?family=Inter:wght@700;800&family=Figtree:wght@400;500&family=Oswald:wght@500&display=swap">
<style>
  :root {
    --flyer-red: #e4472f;
    --ink: #0e0e0e;
    --paper: #ffffff;
    --ring-pink: #f2a3a0;
    --stage-navy: #141a3d;
    --stage-blue: #2e4aa8;
    --backdrop: #e9e7e4;
    --portrait-grey: #d9d9dc;
  }
  * { margin: 0; padding: 0; box-sizing: border-box; }
  html, body { width: 1200px; height: 1006px; overflow: hidden; }
  body { background: var(--backdrop); position: relative; }

  .flyer {
    position: absolute; left: 257px; top: 23px;
    width: 686px; height: 960px;
    background: var(--flyer-red);
    overflow: hidden;
    color: var(--paper);
  }
  .flyer__hero { position: absolute; left: 0; top: 0; }

  .flyer__title {
    position: absolute; left: 32px; top: 238px;
    font-family: "Inter", Arial, sans-serif; font-weight: 800;
    font-size: 56px; line-height: 58px; letter-spacing: 0.5px;
    white-space: nowrap;
  }
  .flyer__title .title-main { display: block; }
  .flyer__title .title-sub { display: block; font-size: 45px; letter-spacing: -0.5px; }

  .speaker-portrait {
    position: absolute; left: 398px; top: 208px;
    width: 268px; height: 268px; border-radius: 50%;
    border: 11px solid var(--ring-pink);
    background: radial-gradient(circle at 50% 40%, #f6f6f6 0%, var(--portrait-grey) 60%, #5d6067 100%);
  }

  .flyer__subtitle {
    position: absolute; left: 32px; top: 407px;
    font-family: "Inter", Arial, sans-serif; font-weight: 700;
    font-size: 32px; line-height: 36px;
  }

  .flyer__body {
    position: absolute; left: 32px; top: 521px; width: 624px;
    font-family: "Figtree", Arial, sans-serif; font-weight: 400;
    font-size: 14.3px; line-height: 17.7px; text-align: justify;
  }
  .flyer__body p + p { margin-top: 17.7px; }

  .lab {
    position: absolute; background: var(--ink); border-radius: 17px;
    font-family: "Oswald", "Arial Narrow", sans-serif; font-weight: 500;
    font-size: 14px; line-height: 25px; letter-spacing: -0.3px;
    padding: 6px 14px; white-space: nowrap; overflow: hidden;
  }
  .lab .mark { font-size: 0.7em; vertical-align: 0.35em; }
  .lab--one { left: 20px; top: 714px; width: 320px; height: 116px; padding-top: 8px; }
  .lab--two { left: 347px; top: 714px; width: 319px; height: 56px; padding-top: 3px; }
  .lab--three { left: 347px; top: 775px; width: 319px; height: 55px; padding-top: 3px; }

  .flyer__closing {
    position: absolute; left: 32px; top: 838px; width: 624px;
    font-family: "Figtree", Arial, sans-serif; font-size: 14.3px; line-height: 17.7px;
    text-align: justify;
  }

  .flyer__contact-band {
    position: absolute; left: 0; top: 898px; width: 686px; height: 34px;
    background: var(--ink);
    font-family: "Inter", Arial, sans-serif; font-weight: 700; font-size: 13.5px;
    line-height: 34px; text-align: center;
  }
</style>
</head>
<body>
<main class="flyer">
  <svg class="flyer__hero" width="686" height="420" viewBox="0 0 686 420">
    <defs>
      <linearGradient id="stageGradient" x1="0" y1="0" x2="0.6" y2="1">
        <stop offset="0" stop-color="#0b0f24"/>
        <stop offset="0.5" stop-color="#141a3d"/>
        <stop offset="1" stop-color="#2e4aa8"/>
      </linearGradient>
    </defs>
    <path d="M0,0 H686 V184 C420,380 150,410 0,362 Z" fill="url(#stageGradient)"
          role="img" aria-label="Photo of a speaker on a conference stage in front of a large audience"/>
    <path d="M0,364 C150,412 420,382 686,186" fill="none" stroke="#ffffff" stroke-width="4"/>
  </svg>

  <h1 class="flyer__title">
    <span class="title-main">COMMAND</span>
    <span class="title-sub">in Seven Weeks</span>
  </h1>

  <div class="speaker-portrait" role="img" aria-label="Portrait photo of Dr. Marcus L. Brandauer in a grey suit, arms crossed"></div>

  <h2 class="flyer__subtitle">Your systematic<br>self-coaching roadmap to<br>power, impact &amp; your future.</h2>

  <section class="flyer__body">
    <p>Dr. Marcus L. Brandauer is the CEO Emeritus of Alpine Advisory Partners—he made an exit in 2013. He is the award-winning author of 8 books, including "Momentum-By-Design," "Speak Up or Fade" and "The Cantor and the Chairman."</p>
    <p>For the past 20 years he has taught leadership at Harwick University in New York and at KLB (Lindmoor University) to prepare future CEOs and other leaders in business, government , non-profits and the military.</p>
    <p>Now, in a process exclusively designed for VBQ’s next generation of emerging leaders, Marcus unpacks his leadership secrets in 3 action-packed labs reduced to the max:</p>
  </section>

  <div class="lab lab--one">Lab 1. Command in Seven Weeks:<br>The Summit Compass Model<span class="mark">®</span>. Self-Assessment.<br>Self-Leadership: “The Lantern.” 5-Year Vision. 100-Day<br>Catalytic Project.</div>
  <div class="lab lab--two">Lab 2. Guiding Through Words. Relationship:<br>Building Trust. Momentum-By-Design. Cockpit.</div>
  <div class="lab lab--three">Lab 3. Debrief and Scale-Up. Sustainability. Action<br>Tools.</div>

  <p class="flyer__closing">Do you want to build your own future and a life you love? Do you want to jump-start that future and life over 100 days while learning a toolbox of leadership skills, networking with like-minded people and even get some pizza? Then join us.</p>

  <footer class="flyer__contact-band">VBQ Gemeindezentrum, Birkenweg 12, 8000 Zürich | +41 00 555 01 23</footer>
</main>
</body>
</html>
```